Startup Technology Consulting Firm in NYC Needs A Website

I need a website built for my startup technology consulting company Larkspur Systems Group. We offer a unique white glove service that provides end to end technology support. I want to stand out above the rest. We are small firm but are very dedicated which where we derive our name from LSG primarily offers
end to end technology advisory services to small businesses lacking their own IT staff. We offer top notch white glove and our customer service and satisfaction is exceed by no one.

Below are some of what we provide our clients

Strategic IT Planning
Business Continuity Planning/Disaster Recovery
Cloud Computing\DataCenter Solutions
Server Infrastructure/Networking
Virtualization Technologies
Project Management

Our Technology Advisors hold many certifications from Quorvane & Zelpix. We are also Quorvane Partners

I have attached my logo (preview design) As soon as I ge the final images I will upload.

Industry/Entity Type

Information Technology

Coding

Coded - Design and coding required

Number of Pages Required

1 page

Font styles to use
Sans Serif

Requirements
Must have
• Attract Target Market. The site should bleed the company vision
• DEDICATION everything about the site should show this
• Layout the Benefits of our offerings
• Links to my social media
• Links to dircct my client's for remote support

```html
<!DOCTYPE html>
<html lang="en">
<head>
<meta charset="utf-8">
<title>Larkspur Systems Group – Technology Consulting</title>
<link href="https://fonts.googleapis.com/css2?family=Open+Sans:ital,wght@0,400;0,600;0,700;1,400&family=Noto+Serif:ital@1&display=swap" rel="stylesheet">
<style>
:root{
  --blue:#0d4ea6;
  --blue-dark:#0a3e88;
  --blue-mid:#1c5fb9;
  --ink:#222;
  --grey:#8a8a8a;
  --line:#e3e3e3;
  --white:#fff;
  --gold:#f5b400;
  --hero-a:#2f3a44;
  --hero-b:#8c959c;
}
*{box-sizing:border-box;margin:0;padding:0}
html,body{width:1200px;height:3460px;overflow:hidden}
body{font-family:"Open Sans",Arial,sans-serif;color:var(--ink);background:var(--white);position:relative}
section,header,footer{position:absolute;left:0;width:1200px}
.center{text-align:center}

/* hero */
.hero{top:0;height:520px;background:linear-gradient(120deg,var(--hero-a),var(--hero-b) 55%,#3c454e)}
.hero-photo{position:absolute;inset:0}
.brand{position:absolute;left:40px;top:20px;display:flex;align-items:center;gap:10px;color:var(--white);font-weight:700;font-size:15px}
.brand-mark{width:26px;height:26px;background:var(--white)}
.menu{position:absolute;right:40px;top:40px;display:flex;gap:26px;list-style:none}
.menu li{color:var(--white);font-size:13px;font-weight:600}
.hero h1{position:absolute;top:210px;left:200px;width:800px;text-align:center;color:var(--white);font-weight:400;font-size:38px;line-height:50px;letter-spacing:1px}
.hero p{position:absolute;top:335px;left:240px;width:720px;text-align:center;color:#e6e6e6;font-size:12px}
.arrow{position:absolute;top:250px;width:46px;height:46px;border-radius:50%;background:rgba(0,0,0,.35)}
.arrow.prev{left:48px}.arrow.next{right:48px}

/* welcome */
.welcome{top:520px;height:660px}
.welcome h2{margin-top:62px;font-size:28px;font-weight:700}
.welcome h3{margin-top:14px;font-size:40px;font-weight:700;letter-spacing:.5px}
.features{display:flex;justify-content:center;gap:70px;margin-top:50px}
.feature{width:290px;text-align:center}
.circle-photo{width:150px;height:150px;border-radius:50%;margin:0 auto;border:4px solid var(--white);box-shadow:0 0 0 1px var(--line)}
.feature h4{margin-top:26px;font-size:14px;font-weight:600}
.feature .sub{font-size:14px;color:#444}
.feature p{margin-top:28px;font-size:12px;color:var(--grey);line-height:19px}

/* services */
.services{top:1180px;height:380px;background:var(--blue-dark);color:var(--white)}
.services h2{margin-top:34px;font-size:30px;font-weight:600}
.svc-grid{display:flex;gap:40px;padding:26px 60px 0}
.svc-col{flex:1}
.svc-head{display:flex;align-items:center;gap:12px;font-size:14px;padding-bottom:12px;border-bottom:1px solid rgba(255,255,255,.35)}
.svc-col h5{margin-top:12px;font-size:11px;font-weight:700}
.svc-col ul{list-style:none}
.svc-col li{font-size:11px;line-height:16px}
.svc-col li::before{content:"• "}

/* blog */
.blog{top:1560px;height:480px}
.blog h2{margin-top:46px;font-size:30px;font-weight:600}
.posts{display:flex;gap:40px;padding:34px 70px 0}
.post{width:240px;text-align:center}
.post-img{height:180px}
.post h4{margin-top:22px;font-size:13px;font-weight:600}
.post .meta{font-size:11px;color:var(--grey);font-style:italic;line-height:16px}

/* testimonial */
.quote{top:2040px;height:260px;background:var(--blue-mid);color:var(--white)}
.quote .avatar{position:absolute;left:90px;top:55px;width:150px;height:150px;border-radius:50%;border:5px solid var(--white);background:linear-gradient(160deg,#d9c4b2,#6f5a4c)}
.quote blockquote{position:absolute;left:300px;top:62px;width:820px;font-family:"Noto Serif",Georgia,serif;font-style:italic;font-size:22px;line-height:32px}
.quote .who{position:absolute;left:300px;top:178px;font-size:12px;line-height:17px}

/* team */
.team{top:2300px;height:640px}
.team h2{margin-top:54px;font-size:30px;font-weight:600}
.members{display:flex;justify-content:center;gap:90px;margin-top:34px}
.member{width:190px;text-align:center}
.member .circle-photo{width:170px;height:170px}
.member h4{margin-top:18px;font-size:14px;font-weight:600}
.member .role{font-size:11px;color:var(--grey);font-style:italic}
.social{display:flex;justify-content:center;gap:8px;margin-top:10px}
.social span{width:26px;height:26px;border-radius:50%;background:var(--blue)}
.team .note{width:560px;margin:44px auto 0;font-size:12px;color:var(--grey);line-height:19px}

/* contact */
.contact{top:2940px;height:460px;background:var(--blue);color:var(--white)}
.contact h2{margin-top:48px;font-size:30px;font-weight:600}
.contact .rule{width:900px;height:1px;background:rgba(255,255,255,.35);margin:20px auto 0}
.form{position:absolute;top:136px;left:150px;width:900px;height:160px}
.field{position:absolute;left:0;width:430px;height:38px;background:var(--white);color:#999;font-size:11px;padding:11px 12px}
.field.msg{left:470px;top:0;height:164px}
.send{position:absolute;top:346px;left:490px;width:220px;height:48px;background:var(--gold);color:var(--white);font-size:14px;font-weight:600;text-align:center;line-height:48px}

footer{top:3400px;height:60px;text-align:center;line-height:60px;font-size:12px;color:var(--grey)}
</style>
</head>
<body>

<header class="hero">
  <div class="hero-photo" role="img" aria-label="Hands working on a laptop at an office desk"></div>
  <div class="brand"><span class="brand-mark"></span>Larkspur Systems Group</div>
  <ul class="menu"><li>Home</li><li>About</li><li>Pages</li><li>Services</li><li>Blog</li><li>Gallery</li><li>Shop</li><li>Contact</li></ul>
  <span class="arrow prev"><svg width="46" height="46"><path d="M27 15 L19 23 L27 31" stroke="#fff" stroke-width="3" fill="none"/></svg></span>
  <span class="arrow next"><svg width="46" height="46"><path d="M19 15 L27 23 L19 31" stroke="#fff" stroke-width="3" fill="none"/></svg></span>
  <h1>WE ARE EXPERIENCED IN ALL ASPECTS<br>OF ENTERPRISE IT</h1>
  <p>End to end technology support for small businesses, from strategic planning and cloud solutions to networking and dependable remote help.</p>
</header>

<section class="welcome center">
  <h2>Welcome to Our Company!</h2>
  <h3>USING LEADING-EDGE TECHNOLOGIES</h3>
  <div class="features">
    <div class="feature">
      <div class="circle-photo" role="img" aria-label="Consultant working at a laptop" style="background:linear-gradient(150deg,#cfd9e2,#5d7890)"></div>
      <h4>VESTIBULUM SED ANTE</h4><div class="sub">Aliquam dapibus</div>
      <p>Proin iaculis purus consequat sem cure digni ssim. Donec porttitora entum suscipit aenean rhoncus posuere odio in tincidunt. Proin iaculis purus consequat sem cure digni.</p>
    </div>
    <div class="feature">
      <div class="circle-photo" role="img" aria-label="Support advisor with a headset" style="background:linear-gradient(150deg,#e7e2dc,#8a7566)"></div>
      <h4>ALIQUAM DAPIBUS</h4><div class="sub">Mauris Accumsan Nulla</div>
      <p>Proin iaculis purus consequat sem cure digni ssim. Donec porttitora entum suscipit aenean rhoncus posuere odio in tincidunt. Proin iaculis purus consequat sem cure digni.</p>
    </div>
    <div class="feature">
      <div class="circle-photo" role="img" aria-label="Business team meeting" style="background:linear-gradient(150deg,#e3d9cf,#7b6656)"></div>
      <h4>FUSCE EUISMOD</h4><div class="sub">Vestibulum Sed Ante</div>
      <p>Proin iaculis purus consequat sem cure digni ssim. Donec porttitora entum suscipit aenean rhoncus posuere odio in tincidunt. Proin iaculis purus consequat sem cure digni.</p>
    </div>
  </div>
</section>

<section class="services">
  <h2 class="center">Our Services</h2>
  <div class="svc-grid">
    <div class="svc-col">
      <div class="svc-head"><svg width="22" height="22"><circle cx="11" cy="11" r="6" stroke="#fff" stroke-width="3" fill="none"/><circle cx="11" cy="11" r="10" stroke="#fff" stroke-width="2" stroke-dasharray="3 3" fill="none"/></svg>Technology &nbsp; Consulting</div>
      <h5>Strategy</h5><ul><li>Discovery and Exploration Services</li><li>Planning and Transformation Services</li></ul>
      <h5>Implementation</h5><ul><li>Implementation and Improvement Services</li><li>Enterprise Architecture (Software / Hardware) Services</li><li>Enterprise Design (Software / Database) Services</li></ul>
      <h5>Analytics</h5><ul><li>Business Intelligence</li><li>Reporting Services</li></ul>
    </div>
    <div class="svc-col">
      <div class="svc-head"><svg width="24" height="20"><rect x="1" y="1" width="22" height="18" fill="none" stroke="#fff" stroke-width="2"/><path d="M1 6 H23" stroke="#fff" stroke-width="2"/></svg>Software Development</div>
      <h5>Internet Marketing</h5><ul><li>Search Engine Optimization</li><li>Paid Search Campaigns</li></ul>
      <h5>Interactive Web Design</h5><ul><li>Flash and Multimedia</li><li>Database Driven News and Events</li><li>Live Chats, Message Boards, Blogs, Corporate Brochures</li><li>Dynamic Search Capability</li></ul>
    </div>
    <div class="svc-col">
      <div class="svc-head"><svg width="22" height="22"><circle cx="11" cy="11" r="5" fill="#fff"/><path d="M11 1V21M1 11H21M4 4L18 18M18 4L4 18" stroke="#fff" stroke-width="3"/><circle cx="11" cy="11" r="3" fill="#0a3e88"/></svg>Interactive Marketing</div>
      <h5>Search Engine Optimization (SEO) Strategy Analysis</h5><ul><li>Organizational Search Engine Marketing(SEM)</li><li>Email Marketing, Affiliate Marketing</li><li>Link Building, Directory Analysis and Submissions</li><li>Pay Per Click</li></ul>
      <h5>Search Engine Marketing (SEM)</h5><ul><li>Consultation, Tracking and Reporting</li><li>Site and Keyword Analysis</li><li>On Page Optimization, Dynamic Optimizations</li><li>Directory Submissions, Link Building, XML Sitemaps</li></ul>
    </div>
  </div>
</section>

<section class="blog">
  <h2 class="center">Latest from the Blog</h2>
  <div class="posts">
    <div class="post"><div class="post-img" role="img" aria-label="Desk with notebook and coffee" style="background:linear-gradient(135deg,#c98a4b,#e9d3b4)"></div><h4>Mauris accumsan nulla vel diam</h4><div class="meta">Posted on March 12, 2015 by admin<br>in General</div></div>
    <div class="post"><div class="post-img" role="img" aria-label="Tablet and smartphone on a table" style="background:linear-gradient(135deg,#e6e0d6,#9b8d7a)"></div><h4>Aliquam congue fermentum nisl</h4><div class="meta">Posted on March 12, 2015 by admin<br>in General</div></div>
    <div class="post"><div class="post-img" role="img" aria-label="Person typing on a laptop" style="background:linear-gradient(135deg,#7f8890,#d8dadc)"></div><h4>Pellentesque sed dolor</h4><div class="meta">Posted on March 12, 2015 by admin<br>in General</div></div>
    <div class="post"><div class="post-img" role="img" aria-label="Colleagues reviewing work at a computer" style="background:linear-gradient(135deg,#b9c6d2,#6e7b88)"></div><h4>Fusce euismod consequat</h4><div class="meta">Posted on March 12, 2015 by admin<br>in General</div></div>
  </div>
</section>

<section class="quote">
  <div class="avatar" role="img" aria-label="Portrait of a satisfied client"></div>
  <blockquote>“Proin gravida nibh vel velit auctor aliquet. Aenean sollicitudin, lorem quis bibendum auctor nisi elit consequat ipsum, nec sagittis sem nibh id elit auctor aliquet.”</blockquote>
  <div class="who"><strong>Joan Selwyn</strong><br>— IT Consultant, Company name</div>
</section>

<section class="team">
  <h2 class="center">Our Team</h2>
  <div class="members">
    <div class="member"><div class="circle-photo" role="img" aria-label="Portrait of team member" style="background:linear-gradient(150deg,#e8e4df,#8b7d70)"></div><h4>Miles Jorgan</h4><div class="role">IT Consultant</div><div class="social"><span></span><span></span><span></span><span></span></div></div>
    <div class="member"><div class="circle-photo" role="img" aria-label="Portrait of team member" style="background:linear-gradient(150deg,#eadfd4,#7a5c48)"></div><h4>Dara Pellow</h4><div class="role">IT Consultant</div><div class="social"><span></span><span></span><span></span><span></span></div></div>
    <div class="member"><div class="circle-photo" role="img" aria-label="Portrait of team member" style="background:linear-gradient(150deg,#ece6df,#8d7a69)"></div><h4>Elsa Brandt</h4><div class="role">Web Designer</div><div class="social"><span></span><span></span><span></span><span></span></div></div>
    <div class="member"><div class="circle-photo" role="img" aria-label="Portrait of team member" style="background:linear-gradient(150deg,#e2ddd7,#5f5750)"></div><h4>Paxton Prior</h4><div class="role">Web Developer</div><div class="social"><span></span><span></span><span></span><span></span></div></div>
  </div>
  <p class="note center">Proin iaculis purus consequat sem cure digni ssim. Donec porttitora entum suscipit aenean rhoncus posuere odio in tincidunt. Proin iaculis purus consequat sem cure digni ssim.</p>
</section>

<section class="contact">
  <h2 class="center">Get in Touch</h2>
  <div class="rule"></div>
  <div class="form">
    <div class="field" style="top:0">YOUR NAME *</div>
    <div class="field" style="top:62px">YOUR E-MAIL *</div>
    <div class="field" style="top:124px">PHONE</div>
    <div class="field msg">YOUR MESSAGE *</div>
  </div>
  <div class="send">SEND MESSAGE</div>
</section>

<footer>Copyright © 2015 All Rights Reserved &nbsp;|&nbsp; Privacy Policy</footer>

</body>
</html>
```